Poster/Flyer design for a Church Youth Group Event

We need a flyer for Pathway Rally 2013. This event is being put on by 6 different churches. The event is for youth from 6th grade to 12th grade. The theme for this event is "Walk In Trust" this is taken from Hebrews 11:1-39.
This flyer will be put up in both schools and the churches. It will also be included with the registration forms for the event.

Target Market(s)

Youth - Ages 11-18

Industry/Entity Type

Church

Requirements
Must have
• We would like the phrases "Walk In Trust" and "Pathway Rally 2013" to be the focal point of the flyer. We would also like the the verse "Hebrews 11:1-39" on the flyer as well.
The date for the event - Feb. 6, 8-10
Cost - $25
There is some additional information that needs to be on the flyer as well:
Speaker - Dr. Marcus Dunbar
Worship Leader - Sam Okafor
I've included pictures of the speaker and the worship leader. It would be nice to have the pics on the flyer, but it is not essential.

We need the names of the churches involved: FBC Cedar Hollow, Marlow Methodist, FBC Marlow, Briar Baptist, Sable Creek Valley C of C, & Cedar Hollow C of C. It doesn't really matter where or how these are on the design, as long as it is there

The flyer also needs to say "registration forms can be picked up in the office or from one of the churches"

I have included a picture of the t-shirt for the event. A similar design style would be great.

```html
<!DOCTYPE html>
<html lang="en">
<head>
<meta charset="utf-8">
<title>Pathway Rally 2013 – Walk In Trust</title>
<link href="https://fonts.googleapis.com/css2?family=Lilita+One&display=swap" rel="stylesheet">
<style>
  :root {
    --ink: #1a1410;
    --cream: #f8ecd0;
    --rose: #e9a08a;
    --peach: #f6d9b0;
    --orange: #ee9a5e;
    --coral: #e07a63;
    --white: #fffaf2;
  }
  * { margin: 0; padding: 0; box-sizing: border-box; }
  html, body { width: 848px; height: 1200px; overflow: hidden; }
  body {
    position: relative;
    font-family: "Lilita One", "Arial Rounded MT Bold", sans-serif;
    color: var(--ink);
    background:
      radial-gradient(ellipse 60% 45% at 15% 80%, rgba(224,122,99,.75), transparent 70%),
      radial-gradient(ellipse 50% 40% at 85% 45%, rgba(238,154,94,.55), transparent 70%),
      radial-gradient(ellipse 55% 35% at 20% 15%, rgba(238,154,94,.6), transparent 70%),
      radial-gradient(ellipse 70% 50% at 60% 70%, rgba(250,226,180,.8), transparent 75%),
      linear-gradient(160deg, var(--peach) 0%, #f3c99a 45%, #eeb48c 75%, var(--peach) 100%);
  }
  .event-title {
    position: absolute; left: 0; right: 0; top: 100px;
    text-align: center; font-size: 92px; line-height: 1;
    color: var(--cream); letter-spacing: -1px;
    -webkit-text-stroke: 10px var(--ink); paint-order: stroke fill;
  }
  .event-year {
    position: absolute; left: 0; right: 0; top: 222px;
    text-align: center; font-size: 86px; line-height: 1; color: var(--ink);
  }
  .theme-ornament {
    position: absolute; left: 118px; top: 280px; width: 612px; height: 370px;
    border-radius: 50% 50% 46% 46%;
    background: radial-gradient(ellipse at center, rgba(60,30,20,.55) 0%, rgba(80,40,25,.35) 45%, rgba(80,40,25,0) 72%);
  }
  .theme-title {
    position: absolute; left: 0; right: 0; top: 428px;
    text-align: center; font-size: 86px; line-height: 1;
    color: var(--rose); letter-spacing: -1px;
    -webkit-text-stroke: 9px var(--ink); paint-order: stroke fill;
  }
  .theme-verse {
    position: absolute; left: 0; right: 0; top: 532px;
    text-align: center; font-size: 28px; color: var(--ink);
  }
  .event-month, .event-days {
    position: absolute; left: 0; right: 0; text-align: center; line-height: 1;
    font-size: 78px; color: var(--ink);
  }
  .event-month { top: 685px; }
  .event-days { top: 775px; }
  .portrait {
    position: absolute; border-radius: 48%;
    background: radial-gradient(ellipse at center, #5a3a2a 0%, #8a5a40 45%, rgba(246,217,176,0) 72%);
  }
  .portrait--speaker { left: 52px; top: 868px; width: 128px; height: 156px; }
  .portrait--leader {
    left: 668px; top: 866px; width: 152px; height: 178px; border-radius: 46%;
    background: radial-gradient(ellipse at center, #3b2c2a 0%, #6d4a52 40%, #c48aa0 62%, rgba(246,217,176,0) 76%);
  }
  .role { position: absolute; line-height: 1; }
  .role__label { display: block; font-size: 25px; }
  .role__name { display: block; font-size: 34px; margin-top: 8px; margin-left: 26px; }
  .role--speaker { left: 176px; top: 888px; }
  .role--leader { left: 462px; top: 892px; }
  .event-cost {
    position: absolute; left: 0; right: 0; top: 1012px;
    text-align: center; font-size: 36px; line-height: 1;
  }
  .host-churches {
    position: absolute; left: 0; right: 0; top: 1074px;
    list-style: none; text-align: center; font-size: 23px; line-height: 32px;
    color: var(--white);
    -webkit-text-stroke: 4px #6b3a26; paint-order: stroke fill;
  }
  .host-churches li { display: inline-block; margin: 0 13px; }
  .registration-note {
    position: absolute; left: 0; right: 0; top: 1154px;
    text-align: center; font-size: 18px; text-transform: uppercase; letter-spacing: .3px;
  }
</style>
</head>
<body>
  <h1 class="event-title">PATHWAY RALLY</h1>
  <div class="event-year">2013</div>

  <div class="theme-ornament" role="img" aria-label="Black tribal flourish ornament framing the event theme"></div>
  <h2 class="theme-title">WALK IN TRUST</h2>
  <div class="theme-verse">Heb. 11:1-39</div>

  <div class="event-month">February</div>
  <div class="event-days">6, 8-10</div>

  <div class="portrait portrait--speaker" role="img" aria-label="Photo of the speaker, Dr. Marcus Dunbar"></div>
  <div class="role role--speaker">
    <span class="role__label">Speaker</span>
    <span class="role__name">Dr. Marcus Dunbar</span>
  </div>

  <div class="role role--leader">
    <span class="role__label">Worship Leader</span>
    <span class="role__name">Sam Okafor</span>
  </div>
  <div class="portrait portrait--leader" role="img" aria-label="Photo of the worship leader, Sam Okafor, playing guitar"></div>

  <div class="event-cost">Cost - $25</div>

  <ul class="host-churches">
    <li>FBC Cedar Hollow</li><li>Marlow Methodist</li><li>FBC Marlow</li><li>Briar Baptist</li><br>
    <li>Sable Creek Valley C of C</li><li>Cedar Hollow C of C</li>
  </ul>

  <p class="registration-note">Registration forms can be picked up in the office or from one of the churches</p>
</body>
</html>
```